Business Cards and Logo

KWM - Personal Injury Attorneys is the name of the firm.
We are personal injury lawyers. We want a crisp, modern and impactful design.
Color schemes are white, matte black and light grey OR white, matte black and red OR white, matte black and a nice blue or yellow.
For logo - we don’t want typical logos like scales of justice or a hammer. We want a general design with the KWM letters.
Target Market(s)
People who need attorneys.
Industry/Entity Type
Law Firm
Contact Information for Business Card
Back side: text: Los Angeles - Santa Ana - San Diego - San Francisco
Front side
Name of firm and logo.
Marco Feltrovski
812 W. Colter Ave. 4th Floor
Glendale, CA 91207
(818)555-0172 (c)
(818)555-0194 (o)
Marco@fieldcounselwest.example
Logo Text
KWM
Font styles to use
Other font styles liked:
- Musk - regular. Military - regular. Moonglade. Future. Or similar fonts.
Requirements
Must have
- See above. Nothing else to provide.
- KWM - Personal Injury Attorneys is the name of the firm.
- We are personal injury lawyers. We want a crisp, modern and impactful design.
- Color schemes are white, matte black and light grey OR white, matte black and red OR white, matte black and a nice blue or yellow.
- For logo - we don’t want typical logos like scales of justice or a hammer. We want a general design with the KWM letters.
Nice to have
- See above - nothing else to provide.
Should not have

```html
<!DOCTYPE html>
<html lang="en">
<head>
<meta charset="utf-8">
<title>KWM - Personal Injury Attorneys — Business Card</title>
<link rel="stylesheet" href="https://fonts.googleapis.com/css2?family=Oswald:wght@400;500;600&family=Lato:wght@300;400&display=swap">
<style>
  :root {
    --page: #2a2a2a;
    --card: #111112;
    --card-edge: #1c1c1e;
    --white: #ffffff;
    --grey: #9a9a9e;
    --faint: #1d1d1f;
    --rule: #3a3a3d;
    --red: #d81e3c;
  }
  * { margin: 0; padding: 0; box-sizing: border-box; }
  html, body { width: 1200px; height: 900px; overflow: hidden; }
  body {
    background: var(--page);
    position: relative;
    font-family: "Lato", sans-serif;
  }
  .card {
    position: absolute;
    left: 300px;
    width: 600px;
    height: 343px;
    background: var(--card);
    border: 1px solid var(--card-edge);
    border-radius: 22px;
    overflow: hidden;
  }
  .card--back { top: 87px; }
  .card--front { top: 470px; }

  /* Back side */
  .back-mark {
    position: absolute;
    top: 92px;
    left: 0;
    width: 100%;
    text-align: center;
    font-family: "Oswald", sans-serif;
    font-weight: 600;
    font-size: 96px;
    line-height: 1;
    letter-spacing: 4px;
    color: var(--white);
  }
  .back-cities {
    position: absolute;
    bottom: 46px;
    left: 0;
    width: 100%;
    text-align: center;
    font-family: "Oswald", sans-serif;
    font-weight: 500;
    font-size: 13px;
    letter-spacing: 0.8px;
    color: var(--white);
  }

  /* Front side */
  .front-watermark {
    position: absolute;
    left: 26px;
    top: 78px;
    font-family: "Oswald", sans-serif;
    font-weight: 600;
    font-size: 150px;
    line-height: 1;
    letter-spacing: 6px;
    color: var(--faint);
  }
  .firm {
    position: absolute;
    right: 34px;
    top: 28px;
    text-align: right;
  }
  .firm-name {
    font-family: "Oswald", sans-serif;
    font-weight: 600;
    font-size: 64px;
    line-height: 1;
    letter-spacing: 3px;
    color: var(--white);
  }
  .firm-tagline {
    margin-top: 6px;
    font-family: "Oswald", sans-serif;
    font-weight: 500;
    font-size: 17px;
    letter-spacing: 1.6px;
    text-transform: uppercase;
    color: var(--white);
  }
  .divider {
    position: absolute;
    left: 232px;
    right: 34px;
    top: 170px;
    height: 1px;
    background: var(--rule);
  }
  .address {
    position: absolute;
    right: 34px;
    top: 186px;
    text-align: right;
    font-weight: 300;
    font-size: 16px;
    line-height: 1.35;
    color: var(--grey);
  }
  .person {
    position: absolute;
    left: 34px;
    bottom: 26px;
  }
  .person-name {
    font-family: "Oswald", sans-serif;
    font-weight: 500;
    font-size: 22px;
    letter-spacing: 0.6px;
    text-transform: uppercase;
    color: var(--red);
    margin-bottom: 8px;
  }
  .contact-list { list-style: none; }
  .contact-item {
    display: flex;
    align-items: center;
    gap: 8px;
    font-size: 15px;
    line-height: 1.4;
    color: var(--white);
  }
  .contact-icon { width: 13px; height: 13px; flex: none; }
</style>
</head>
<body>

  <section class="card card--back" aria-label="Business card, back side">
    <div class="back-mark">KWM</div>
    <p class="back-cities">LOS ANGELES - SANTA ANA - SAN DIEGO - SAN FRANCISCO</p>
  </section>

  <section class="card card--front" aria-label="Business card, front side">
    <div class="front-watermark" aria-hidden="true">KWM</div>

    <div class="firm">
      <div class="firm-name">KWM</div>
      <div class="firm-tagline">Personal Injury Attorneys</div>
    </div>

    <div class="divider"></div>

    <address class="address" style="font-style:normal">
      812 W. Colter Ave. 4th Floor<br>
      Glendale, CA 91207
    </address>

    <div class="person">
      <h1 class="person-name">Marco Feltrovski</h1>
      <ul class="contact-list">
        <li class="contact-item">
          <svg class="contact-icon" viewBox="0 0 13 13" aria-hidden="true">
            <rect x="3" y="0.5" width="7" height="12" rx="1.3" fill="none" stroke="var(--red)" stroke-width="1.4"/>
            <circle cx="6.5" cy="10.3" r="0.8" fill="var(--red)"/>
          </svg>
          (818)555-0172
        </li>
        <li class="contact-item">
          <svg class="contact-icon" viewBox="0 0 13 13" aria-hidden="true">
            <path d="M1 4.5 C1 2 12 2 12 4.5 L10 5.5 L9 4 C7.5 3.5 5.5 3.5 4 4 L3 5.5 Z" fill="var(--red)"/>
            <path d="M3.5 6.5 H9.5 L11 12 H2 Z" fill="var(--red)"/>
          </svg>
          (818)555-0194
        </li>
        <li class="contact-item">
          <svg class="contact-icon" viewBox="0 0 13 13" aria-hidden="true">
            <rect x="0.5" y="2.5" width="12" height="8.5" fill="var(--red)"/>
            <path d="M0.8 3 L6.5 7.5 L12.2 3" fill="none" stroke="var(--card)" stroke-width="1"/>
          </svg>
          Marco@fieldcounselwest.example
        </li>
      </ul>
    </div>
  </section>

</body>
</html>
```